Health and Wellness. I am an energetic, but not over the top, Certified Personal Trainer and Nutriti

I need a flyer, 8.5 x 11, representing my company to be displayed in a Doctor's office that specializes in Pain Medicine. Most, if not all, of these clients experience pain or have some chronic diseases such as high blood pressure, high cholesterol, back pain, joint pain, etc. So the flyer should convey that exercise and nutrition reduce/relieves pain and references some of these ailments. Ideally, the flyer should depict an overweight person exercising with a content, or somewhat content or smiling expression on their face in some part of the flyer. My services cover nutrition and include personal training to where I Ideally train people in their home, equipment permitting, or outside in our local Floridian Parks, and sometimes beaches. This flyer will be in a display case, and the bottom right 8.5 x5 cm will need to be blank, or allow for me to input the back of my business car into it, as I'll have business cards readily available in front of the flyer to be taken. I've included some versions of my logos to be added to the flyer. The other picture is of the flyer holder, with business card area, that this flyer will be presented in. Finally, I've attached a pic of what the back of my business card looks like to be input into that bottom right hand corner. You'll be able to see the area in the bottom right that will display my business cards.
Target Market(s)
People looking for weight loss through Nutrition and Fitness. Those looking to relieve joint and/or back pain or those with Chronic diseases such as high blood pressure, high cholesterol, etc.
Industry/Entity Type
Doctor
Requirements
Must have
- Resemble my Logo's color scheme: Red, Teal, and Grey. Some type of photo of an overweight or slightly overweight person exercising.

```html
<!DOCTYPE html>
<html lang="en">
<head>
<meta charset="UTF-8">
<title>Delmar's Fitness Flyer</title>
<link href="https://fonts.googleapis.com/css2?family=Montserrat:wght@600;700&family=Open+Sans:wght@300;400&display=swap" rel="stylesheet">
<style>
  :root {
    --stage: #d9d9d6;
    --ink: #0b0b0c;
    --panel-top: #1c1c1e;
    --panel-bottom: #050506;
    --accent-red: #e2333f;
    --deep-red: #b3222d;
    --teal: #2aa8a0;
    --title-grey: #a7a9ab;
    --tagline: #e9e9e9;
    --body-grey: #cfcfd1;
    --card-slot-line: #3a3a3e;
  }
  * { margin: 0; padding: 0; box-sizing: border-box; }
  html, body {
    width: 1200px;
    height: 800px;
    overflow: hidden;
    background: var(--stage);
  }
  .canvas {
    position: relative;
    width: 1200px;
    height: 800px;
    display: flex;
    align-items: center;
    justify-content: center;
  }
  .flyer {
    position: relative;
    width: 556px;
    height: 720px;
    background: var(--ink);
    overflow: hidden;
    box-shadow: 0 6px 24px rgba(0,0,0,0.25);
  }
  .hero-photo {
    position: absolute;
    left: 0;
    top: 0;
    width: 100%;
    height: 300px;
    background:
      radial-gradient(ellipse 120px 180px at 50% 62%, #8a5a44 0%, #4a2f24 45%, rgba(10,10,10,0) 100%),
      linear-gradient(180deg, #121212 0%, #0a0a0a 100%);
  }
  .wave {
    position: absolute;
    left: 0;
    top: 0;
    width: 556px;
    height: 720px;
  }
  .brand-mark {
    position: absolute;
    left: 0;
    right: 0;
    top: 318px;
    display: flex;
    align-items: center;
    justify-content: center;
    gap: 12px;
  }
  .brand-mark__ring {
    width: 40px;
    height: 40px;
    border: 4px solid var(--teal);
    border-radius: 50%;
  }
  .brand-mark__name {
    font-family: 'Montserrat', sans-serif;
    font-weight: 700;
    font-size: 19px;
    letter-spacing: 1px;
    color: var(--deep-red);
  }
  .company-name {
    position: absolute;
    left: 0;
    right: 0;
    top: 382px;
    text-align: center;
    font-family: 'Montserrat', sans-serif;
    font-weight: 700;
    font-size: 33px;
    letter-spacing: 2.5px;
    color: var(--title-grey);
    text-transform: uppercase;
  }
  .tagline {
    position: absolute;
    left: 0;
    right: 0;
    top: 438px;
    text-align: center;
    font-family: 'Open Sans', sans-serif;
    font-weight: 300;
    font-size: 20px;
    line-height: 30px;
    color: var(--tagline);
  }
  .relief {
    position: absolute;
    left: 30px;
    top: 526px;
    width: 290px;
  }
  .relief__heading {
    font-family: 'Montserrat', sans-serif;
    font-weight: 600;
    font-size: 15px;
    line-height: 20px;
    color: var(--teal);
    margin-bottom: 10px;
  }
  .relief__list {
    list-style: none;
    font-family: 'Open Sans', sans-serif;
    font-weight: 400;
    font-size: 14px;
    line-height: 24px;
    color: var(--body-grey);
  }
  .relief__list li {
    display: flex;
    align-items: center;
    gap: 10px;
  }
  .relief__list li::before {
    content: "";
    width: 8px;
    height: 8px;
    border-radius: 50%;
    background: var(--accent-red);
    flex: none;
  }
  .card-slot {
    position: absolute;
    right: 0;
    bottom: 0;
    width: 219px;
    height: 129px;
    border-top: 1px dashed var(--card-slot-line);
    border-left: 1px dashed var(--card-slot-line);
  }
</style>
</head>
<body>
  <main class="canvas">
    <article class="flyer">
      <div class="hero-photo" role="img" aria-label="Photo of a person exercising against a dark studio backdrop"></div>

      <svg class="wave" viewBox="0 0 556 720" aria-hidden="true">
        <defs>
          <linearGradient id="lowerPanel" x1="0" y1="0" x2="0" y2="1">
            <stop offset="0" stop-color="#1c1c1e"/>
            <stop offset="1" stop-color="#050506"/>
          </linearGradient>
        </defs>
        <path d="M0 236 Q278 326 556 236 L556 720 L0 720 Z" fill="#e2333f"/>
        <path d="M0 248 Q278 338 556 250 L556 720 L0 720 Z" fill="url(#lowerPanel)"/>
      </svg>

      <div class="brand-mark">
        <span class="brand-mark__ring"></span>
        <span class="brand-mark__name">Delmar's Fitness</span>
      </div>

      <h1 class="company-name">Delmar's Fitness</h1>
      <p class="tagline">Helping you to lose weight, gain muscle,<br>and own the room</p>

      <section class="relief">
        <h2 class="relief__heading">Exercise and nutrition that ease pain</h2>
        <ul class="relief__list">
          <li>Back and joint pain</li>
          <li>High blood pressure</li>
          <li>High cholesterol</li>
          <li>Training at home, parks and beaches</li>
        </ul>
      </section>

      <div class="card-slot" aria-label="Space reserved for business card"></div>
    </article>
  </main>
</body>
</html>
```